依頼詳細
大 横240×縦150×高さ30
中 横240×縦250×高さ30
小 横150×縦100×高さ30  *箱サイズ

上記の包装紙のデザイン

フィルムサイズ 幅90×ピッチ130 *横デザイン

上記のフィルムのデザイン
記載項目
上記のパッケージのサイズでお願いいたします。

*上記包装紙とフィルムのデザイン *サイズ微調整あり)
希望イメージ
希望する色
青系、水色系
納品ファイル
• イラストレーター形式 (.ai)

```html
<!DOCTYPE html>
<html lang="ja">
<head>
<meta charset="utf-8">
<title>MIZORA – Box Wrapping</title>
<link href="https://fonts.googleapis.com/css2?family=Poiret+One&family=Cormorant+Garamond:wght@500&family=Noto+Sans+JP:wght@500&display=swap" rel="stylesheet">
<style>
  :root{
    --bg:#ffffff;
    --teal-light:#73c8ba;
    --teal-face:#6cc3b4;
    --teal-band:#64bdae;
    --teal-dark:#1fa794;
    --ink-light:#ffffff;
    --ink-soft:#e4f6f2;
    --pill:#1b9c8a;
  }
  *{margin:0;padding:0;box-sizing:border-box}
  html,body{width:1200px;height:2700px;overflow:hidden;background:var(--bg)}
  .sheet{position:relative;width:1200px;height:2700px}

  .box{position:absolute}
  .box--large{left:32px;top:32px;width:1128px;height:856px;font-size:16px}
  .box--medium{left:32px;top:912px;width:1128px;height:1136px;font-size:18px}
  .box--small{left:220px;top:2100px;width:740px;height:560px;font-size:10px;--side-left:84%;--face-right:16%}

  .panel{position:absolute}
  .glue-strip{left:0;top:0;width:4.3%;height:90%;background:var(--teal-dark)}
  .top-band{left:4.3%;right:var(--face-right,10.6%);top:0;height:6.5%;background:var(--teal-band)}
  .face{left:4.3%;right:var(--face-right,10.6%);top:6.5%;height:69.5%;background:var(--teal-face);overflow:hidden}
  .front-band{left:4.3%;right:var(--face-right,10.6%);top:76%;height:14%;background:var(--teal-band);
    display:flex;flex-direction:column;align-items:center;justify-content:center;gap:.5em}
  .bottom-flap{left:0;right:var(--face-right,10.6%);top:90%;bottom:0;background:var(--teal-light)}
  .side-panel{left:var(--side-left,90.8%);right:0;top:0;height:89%;background:var(--teal-dark);
    display:flex;align-items:center;justify-content:center;overflow:hidden}

  .ornament{position:absolute;left:50%;top:50%;width:78%;aspect-ratio:1/1;transform:translate(-50%,-52%);
    border-radius:50%;background:radial-gradient(circle,rgba(255,255,255,.18) 0%,rgba(255,255,255,.10) 45%,rgba(255,255,255,0) 70%)}
  .face-content{position:absolute;inset:0;display:flex;flex-direction:column;align-items:center;justify-content:center;text-align:center;color:var(--ink-light)}
  .tagline{font-family:"Cormorant Garamond",serif;font-weight:500;font-size:1.2em;color:var(--ink-soft);letter-spacing:.02em;white-space:nowrap}
  .face-content .tagline{margin-bottom:.8em}
  .brand{font-family:"Poiret One",sans-serif;font-weight:400;font-size:7em;line-height:1;letter-spacing:.08em;color:var(--ink-light);white-space:nowrap}
  .pill{margin-top:1.4em;background:var(--pill);color:var(--ink-light);font-family:"Noto Sans JP",sans-serif;font-weight:500;
    font-size:1em;padding:.15em 1.6em;border-radius:.2em;white-space:nowrap}
  .subtitle{margin-top:.5em;font-family:"Noto Sans JP",sans-serif;font-weight:500;font-size:1.15em;color:var(--ink-light);letter-spacing:.06em;white-space:nowrap}

  .front-band .tagline{font-size:.9em}
  .brand--band{font-family:"Poiret One",sans-serif;font-weight:400;color:var(--ink-light);font-size:2.4em;line-height:1;letter-spacing:.08em;white-space:nowrap}

  .side-pattern{position:absolute;inset:0;background:linear-gradient(180deg,rgba(255,255,255,.05),rgba(255,255,255,0) 40%,rgba(255,255,255,.05))}
  .side-mark{position:absolute;left:50%;top:50%;width:70%;aspect-ratio:1/1;transform:translate(-50%,-50%);
    border:1px solid rgba(255,255,255,.35);border-radius:50%}
  .side-label{position:relative;writing-mode:vertical-rl;font-family:"Cormorant Garamond",serif;font-weight:500;color:var(--ink-light);
    font-size:1.1em;letter-spacing:.2em}
</style>
</head>
<body>
<main class="sheet">

  <section class="box box--large" aria-label="Large box wrapping">
    <div class="panel glue-strip"></div>
    <div class="panel top-band"></div>
    <div class="panel face">
      <div class="ornament" role="img" aria-label="Lace medallion ornament"></div>
      <div class="face-content">
        <p class="tagline">White chocolate biscuits from the high plateau</p>
        <h2 class="brand">MIZORA</h2>
        <p class="pill">一口サイズ</p>
        <p class="subtitle">高原のとろけるショコラ</p>
      </div>
    </div>
    <div class="panel front-band">
      <p class="tagline">White chocolate biscuits from the high plateau</p>
      <p class="brand--band">MIZORA</p>
    </div>
    <div class="panel bottom-flap"></div>
    <div class="panel side-panel">
      <div class="side-pattern" role="img" aria-label="Faint lace pattern"></div>
      <div class="side-mark"></div>
      <p class="side-label">SNACK</p>
    </div>
  </section>

  <section class="box box--medium" aria-label="Medium box wrapping">
    <div class="panel glue-strip"></div>
    <div class="panel top-band"></div>
    <div class="panel face">
      <div class="ornament" role="img" aria-label="Lace medallion ornament"></div>
      <div class="face-content">
        <p class="tagline">White chocolate biscuits from the high plateau</p>
        <h2 class="brand">MIZORA</h2>
        <p class="pill">一口サイズ</p>
        <p class="subtitle">高原のとろけるショコラ</p>
      </div>
    </div>
    <div class="panel front-band">
      <p class="tagline">White chocolate biscuits from the high plateau</p>
      <p class="brand--band">MIZORA</p>
    </div>
    <div class="panel bottom-flap"></div>
    <div class="panel side-panel">
      <div class="side-pattern" role="img" aria-label="Faint lace pattern"></div>
      <div class="side-mark"></div>
      <p class="side-label">SNACK</p>
    </div>
  </section>

  <section class="box box--small" aria-label="Small box wrapping">
    <div class="panel glue-strip"></div>
    <div class="panel top-band"></div>
    <div class="panel face">
      <div class="ornament" role="img" aria-label="Lace medallion ornament"></div>
      <div class="face-content">
        <p class="tagline">White chocolate biscuits from the high plateau</p>
        <h2 class="brand">MIZORA</h2>
        <p class="pill">一口サイズ</p>
        <p class="subtitle">高原のとろけるショコラ</p>
      </div>
    </div>
    <div class="panel front-band">
      <p class="tagline">White chocolate biscuits from the high plateau</p>
      <p class="brand--band">MIZORA</p>
    </div>
    <div class="panel bottom-flap"></div>
    <div class="panel side-panel">
      <div class="side-pattern" role="img" aria-label="Faint lace pattern"></div>
      <div class="side-mark"></div>
      <p class="side-label">SNACK</p>
    </div>
  </section>

</main>
</body>
</html>
```